Used automobile dealer continuing education credits postcard

Brightpath Modules, LLC a Georgia Corportationwww.UsedAutoDealerTraining.comGeorgia Used Auto Dealer Continuing Education (CE) Credits OnlineWe are the first to bring to you ONLINE TRAINING in the State of GeorgiaYou finally have a CHOICE!No More Seminars to attend! No Dues! No HassleWork from your own computer on YOUR time and YOUR schedule. It's fast - Easy - ConvenientTake advantage of the July Special $69.00 Enroll Now and Lock in your savings.These are just ideas that I have given to you for you to use to create the postcard.
Target Market(s)
Used auto dealers in the state of georgia
Industry/Entity Type
Education
Look and feel
Each slider illustrates characteristics of the customer's brand and the style your logo design should communicate.

```html
<!DOCTYPE html>
<html lang="en">
<head>
<meta charset="utf-8">
<title>Brightpath Modules – Georgia Used Auto Dealer CE Postcard</title>
<link rel="stylesheet" href="https://fonts.googleapis.com/css2?family=Bebas+Neue&family=Raleway:wght@300;400;600&family=Kalam:wght@400&family=Roboto+Condensed:wght@700&display=swap">
<style>
  :root {
    --page: #ffffff;
    --blue-deep: #0a5a8c;
    --blue-mid: #1a8fcf;
    --blue-glow: #4fc0f0;
    --white: #ffffff;
    --yellow: #f6df1e;
    --band-black: #050505;
    --price-blue: #36b6ee;
    --gray-light: #f1f1f1;
    --gray-dark: #b9b9b9;
    --brand-blue: #1e86c4;
    --rule: #d6d6d6;
    --stamp-line: #cfcfcf;
  }
  html, body {
    margin: 0;
    padding: 0;
    width: 1200px;
    height: 930px;
    overflow: hidden;
    background: var(--page);
  }
  .canvas {
    position: relative;
    width: 1200px;
    height: 930px;
  }
  .postcard-front {
    position: absolute;
    left: 0;
    top: 0;
    width: 580px;
    height: 765px;
    overflow: hidden;
    background: radial-gradient(ellipse 60% 50% at 40% 48%, var(--blue-glow) 0%, var(--blue-mid) 45%, var(--blue-deep) 100%);
  }
  .headline {
    position: absolute;
    left: 40px;
    top: 44px;
    margin: 0;
    font-family: "Bebas Neue", "Oswald", sans-serif;
    font-weight: 400;
    font-size: 38px;
    line-height: 31px;
    letter-spacing: 0.3px;
    color: var(--white);
  }
  .headline .highlight { color: var(--yellow); }
  .subhead {
    position: absolute;
    left: 40px;
    top: 112px;
    margin: 0;
    font-family: "Raleway", sans-serif;
    font-weight: 300;
    font-size: 28.5px;
    line-height: 31px;
    color: var(--white);
    letter-spacing: 0.2px;
  }
  .photo-placeholder {
    position: absolute;
    left: 178px;
    top: 198px;
    width: 402px;
    height: 437px;
    background: linear-gradient(160deg, rgba(230,238,246,0.55) 0%, rgba(160,190,215,0.45) 55%, rgba(90,130,165,0.4) 100%);
    border-radius: 160px 160px 0 0;
  }
  .swoosh {
    position: absolute;
    left: 0;
    top: 300px;
    width: 300px;
    height: 200px;
  }
  .handnote {
    position: absolute;
    left: 52px;
    top: 300px;
    margin: 0;
    font-family: "Kalam", cursive;
    font-size: 22px;
    line-height: 25px;
    color: var(--white);
    transform: rotate(-9deg);
    transform-origin: left top;
  }
  .offer-band {
    position: absolute;
    left: 0;
    top: 635px;
    width: 580px;
    height: 65px;
    background: var(--band-black);
    color: var(--white);
    text-align: center;
    font-family: "Raleway", sans-serif;
    font-weight: 300;
    font-size: 21px;
    line-height: 25px;
    padding-top: 7px;
    box-sizing: border-box;
  }
  .offer-band p { margin: 0; }
  .offer-band .price {
    color: var(--price-blue);
    font-weight: 600;
  }
  .brand-bar {
    position: absolute;
    left: 0;
    top: 700px;
    width: 580px;
    height: 65px;
    background: linear-gradient(90deg, var(--gray-dark) 0%, var(--gray-light) 25%, var(--gray-light) 75%, var(--gray-dark) 100%);
  }
  .brand-name {
    position: absolute;
    right: 30px;
    top: 14px;
    margin: 0;
    font-family: "Roboto Condensed", sans-serif;
    font-weight: 700;
    font-size: 28px;
    color: var(--brand-blue);
  }
  .postcard-back {
    position: absolute;
    left: 580px;
    top: 0;
    width: 620px;
    height: 765px;
  }
  .stamp-box {
    position: absolute;
    left: 324px;
    top: 30px;
    width: 262px;
    height: 264px;
    border: 2px solid var(--stamp-line);
    box-sizing: border-box;
  }
  .address-line {
    position: absolute;
    left: 75px;
    width: 495px;
    height: 0;
    border-top: 3px solid var(--rule);
  }
</style>
</head>
<body>
<main class="canvas">
  <section class="postcard-front">
    <h1 class="headline">We are the first to bring to you<br><span class="highlight">Online Training</span> in the State of Georgia</h1>
    <p class="subhead">USED AUTO DEALER CONTINUING<br>EDUCATION (CE) CREDITS ONLINE</p>

    <div class="photo-placeholder" role="img" aria-label="Photo of a smiling dealer holding an open laptop"></div>

    <svg class="swoosh" viewBox="0 0 300 200" aria-hidden="true">
      <path d="M190 45 C 110 45, 30 60, 32 95 C 34 130, 120 150, 200 165" fill="none" stroke="#ffffff" stroke-opacity="0.75" stroke-width="3" stroke-linecap="round"/>
    </svg>
    <p class="handnote">Work from your own computer on<br>YOUR time and YOUR schedule.</p>

    <div class="offer-band">
      <p>*Take advantage of the July Special <span class="price">$69.00</span></p>
      <p>Enroll Now and Lock in your savings.</p>
    </div>

    <div class="brand-bar">
      <p class="brand-name">Brightpath Modules, LLC</p>
    </div>
  </section>

  <section class="postcard-back">
    <div class="stamp-box"></div>
    <div class="address-line" style="top:404px"></div>
    <div class="address-line" style="top:488px"></div>
    <div class="address-line" style="top:570px"></div>
    <div class="address-line" style="top:653px"></div>
  </section>
</main>
</body>
</html>
```